yourSmileCare Brookvale Business Card

Please design a two sided business card that is Elegant and Professional
Add subtle elegant patterns to suit Spot UV printing/ or raised printing

Name: Dr Marcus T. Fenwick
Qualification: BDSc (QLD)
Title: Dental Surgeon, Clinical Director
Company: yourSmileCare Brookvale
Phone: (02) 7593 2268
Address: Shop 7/18-20 Lindon Ave Brookvale 2097
email: info@yoursmilecarebrookvale.com.au
Facebook: facebook.com/yoursmilecarebrookvale

Motto:
Quality dentistry you can trust

Description of services (not compulsory):
Preventative Dentistry | General Dentistry
Cosmetic Dentistry | Teeth Whitening
Crown and Bridge | Root Canal Therapy
Veneers | Clearvono | Orthodontics
Emergency Dental Care | After Hours

Personalised Treatment Plans
Transparent Fees

Please make sure card is elegant and professional

Target Market(s)

general population, patients,
Dental sales companies, other professions

Industry/Entity Type

Dental Clinic

Contact Information for Business Card

Name: Dr Marcus T. Fenwick
Qualification: BDSc (QLD)
Phone: (02) 7593 2268
Address: Shop 7/18-20 Lindon Ave Brookvale

Motto:

Description of services (not compulsory)

Transparent Fees

Image of dental surgery optional

Please make sure card is elegant and profession

Requirements
Must have
• Logo
• Name, Title (next to name), Business
• Phone, address, facbeook
• Must have stylish design to suit SPOT UV reflective printing
Nice to have
• Subtle elegant patterns which will have Spot UV on them when printed
• Colours to match logo colour
• Description of services
Should not have
• Small fonts that are hard to read
• DO NOT PUT IMAGES OF DENTAL INSTRUMENTS OR TEETH PLEASE

```html
<!DOCTYPE html>
<html lang="en">
<head>
<meta charset="utf-8">
<title>yourSmileCare Brookvale – Business Card</title>
<link rel="stylesheet" href="https://fonts.googleapis.com/css2?family=Open+Sans:wght@400;600;700&display=swap">
<style>
  :root {
    --bg: #b9babd;
    --card-white: #ffffff;
    --brand-green: #8bbf43;
    --green-deep: #76a837;
    --text-grey: #5f6062;
    --rule-grey: #a9aaac;
    --social-square: #3b5a98;
  }
  * { box-sizing: border-box; margin: 0; padding: 0; }
  html, body {
    width: 1200px; height: 1200px; overflow: hidden;
    background: var(--bg);
    font-family: "Open Sans", sans-serif;
  }
  .canvas {
    width: 1200px; height: 1200px;
    display: flex; flex-direction: column;
    align-items: center; justify-content: center; gap: 48px;
  }
  .card {
    position: relative;
    width: 900px; height: 514px;
    box-shadow: 0 10px 30px rgba(0,0,0,0.18);
  }

  /* Back side */
  .card-back { background: var(--brand-green); }
  .motto {
    position: absolute; left: 90px; top: 70px;
    color: var(--green-deep);
    font-weight: 700; line-height: 1.05;
    letter-spacing: 3px;
    text-shadow: 0 1px 0 rgba(255,255,255,0.12), 0 -1px 0 rgba(0,0,0,0.08);
  }
  .motto span { display: block; font-size: 72px; }
  .motto .motto-strong { font-size: 100px; }

  /* Front side */
  .card-front { background: var(--card-white); color: var(--text-grey); }
  .brand {
    position: absolute; right: 50px; top: 90px;
    display: flex; align-items: center; gap: 18px;
    color: var(--brand-green); font-weight: 600;
  }
  .brand-dot { width: 34px; height: 34px; border-radius: 50%; background: var(--brand-green); }
  .brand-name { text-align: right; line-height: 1; }
  .brand-name .brand-main { display: block; font-size: 58px; letter-spacing: -1px; }
  .brand-name .brand-place { display: block; font-size: 34px; letter-spacing: 6px; margin-top: 8px; }

  .person { position: absolute; left: 60px; top: 255px; }
  .person-name { color: var(--brand-green); font-weight: 600; font-size: 34px; }
  .person-name .qual { color: var(--text-grey); font-weight: 400; font-size: 19px; margin-left: 6px; }
  .person-title { font-size: 21px; margin-top: 2px; }

  .contact { list-style: none; font-size: 20px; }
  .contact li { display: flex; align-items: center; gap: 10px; height: 34px; }
  .contact svg { width: 18px; height: 18px; flex: none; }
  .contact-left { position: absolute; left: 60px; top: 352px; }
  .contact-right { position: absolute; left: 460px; top: 425px; }
  .social-square { width: 17px; height: 17px; background: var(--social-square); border-radius: 2px; flex: none; }

  .rule { position: absolute; left: 460px; right: 50px; top: 408px; height: 1px; background: var(--rule-grey); }
</style>
</head>
<body>
<main class="canvas">
  <section class="card card-back" aria-label="Business card back">
    <p class="motto">
      <span>Quality</span>
      <span>Dentistry</span>
      <span>You Can</span>
      <span class="motto-strong">Trust</span>
    </p>
  </section>

  <section class="card card-front" aria-label="Business card front">
    <div class="brand">
      <div class="brand-dot"></div>
      <div class="brand-name">
        <span class="brand-main">yourSmileCare</span>
        <span class="brand-place">BROOKVALE</span>
      </div>
    </div>

    <div class="person">
      <p class="person-name">Dr Marcus T. Fenwick <span class="qual">BDSc (QLD)</span></p>
      <p class="person-title">Dental Surgeon, Clinical Director</p>
    </div>

    <ul class="contact contact-left">
      <li>
        <svg viewBox="0 0 24 24" aria-hidden="true"><path fill="#8bbf43" d="M6.6 10.8a15.1 15.1 0 0 0 6.6 6.6l2.2-2.2a1 1 0 0 1 1-.25 11.4 11.4 0 0 0 3.6.57 1 1 0 0 1 1 1V20a1 1 0 0 1-1 1A17 17 0 0 1 3 4a1 1 0 0 1 1-1h3.5a1 1 0 0 1 1 1c0 1.25.2 2.45.57 3.57a1 1 0 0 1-.25 1z"/></svg>
        (02) 7593 2268
      </li>
      <li>
        <svg viewBox="0 0 24 24" aria-hidden="true"><path fill="#8bbf43" d="M3 6h18v12H3z"/><path fill="none" stroke="#fff" stroke-width="1.6" d="M3.5 6.5 12 13l8.5-6.5"/></svg>
        info@yoursmilecarebrookvale.com.au
      </li>
    </ul>

    <div class="rule"></div>

    <ul class="contact contact-right">
      <li><span class="social-square"></span>yoursmilecarebrookvale</li>
      <li>
        <svg viewBox="0 0 24 24" aria-hidden="true"><path fill="#8bbf43" d="M12 2a7 7 0 0 0-7 7c0 5.2 7 13 7 13s7-7.8 7-13a7 7 0 0 0-7-7zm0 9.5A2.5 2.5 0 1 1 12 6.5a2.5 2.5 0 0 1 0 5z"/></svg>
        Shop 7/18-20 Lindon Ave Brookvale
      </li>
    </ul>
  </section>
</main>
</body>
</html>
```